Business Card needed for Drainora, a growing Septic Service company

Drainora, a growing local septic service company in Pennsylvania, needs updated business cards. We'd like the business card to feature our logo and communicate that we provide Septic Pumping, Installations/Repairs, Restroom Rentals, and 24/7 Emergency Service. The business card should be eye-catching, bold, and clean/simple. We have been in business almost 10 years and would like to expand and update our business brand and image.

Target Market(s)

Residential and Commercial, New and Current Homeowners

Industry/Entity Type

Service

Contact Information for Business Card

Contact on the business card should be: Dale Pruitt Owner & Operator
Phone: 610-555-0187
Email: service@drainora.example
Website: www.drainora.example
Address: 812 Birchwell Lane Fernwick PA 18999

Font styles to use
Sans Serif

Colors

Designer to choose colors to be used in the design.

Requirements
Must have
• Feature logo on both side of business card.
Nice to have
• We envision the contact information on one side and our services listed on the other side. Utilize the green from the symbol in our logo as part of the design, overall design color scheme should be white, grey, black.

```html
<!DOCTYPE html>
<html lang="en">
<head>
<meta charset="utf-8">
<title>Drainora Business Card</title>
<link href="https://fonts.googleapis.com/css2?family=Noto+Sans:wght@400;600;800&display=swap" rel="stylesheet">
<style>
  :root {
    --page-bg: #ececec;
    --card-bg: #f7f7f7;
    --ink: #141414;
    --text: #3c3c3c;
    --green: #7cc242;
    --divider: #c9c9c9;
  }
  * { margin: 0; padding: 0; box-sizing: border-box; }
  html, body { width: 1200px; height: 900px; overflow: hidden; }
  body {
    background: var(--page-bg);
    font-family: "Noto Sans", Arial, sans-serif;
    display: flex;
    flex-direction: column;
    align-items: center;
    justify-content: center;
    gap: 60px;
  }
  .card {
    position: relative;
    width: 560px;
    height: 320px;
    background: var(--card-bg);
    border-radius: 22px;
    box-shadow: 0 2px 10px rgba(0,0,0,0.10);
    display: flex;
    align-items: center;
  }
  .brand {
    width: 280px;
    display: flex;
    align-items: center;
    justify-content: center;
    gap: 8px;
  }
  .brand-square {
    width: 32px;
    height: 32px;
    background: var(--green);
  }
  .brand-name {
    font-weight: 800;
    font-size: 27px;
    letter-spacing: 0.5px;
    color: var(--ink);
    text-transform: uppercase;
  }
  .divider {
    position: absolute;
    left: 280px;
    top: 90px;
    bottom: 90px;
    width: 1px;
    background: var(--divider);
  }
  .card--front .divider { top: 95px; bottom: 95px; }
  .card--back .divider { top: 90px; bottom: 80px; }
  .details {
    padding-left: 32px;
    color: var(--text);
    font-size: 12.5px;
    line-height: 18px;
  }
  .services { list-style: none; margin-top: -10px; }
  .services li { display: flex; align-items: center; gap: 8px; }
  .services li::before {
    content: "";
    width: 4px; height: 4px;
    background: var(--green);
  }
  .person-name {
    color: var(--green);
    font-weight: 600;
    font-size: 16px;
    line-height: 20px;
  }
  .person-role { margin-bottom: 17px; }
  .address { margin-bottom: 15px; }
  .contact { list-style: none; }
  .contact li { display: flex; align-items: center; gap: 7px; }
  .contact svg { width: 11px; height: 11px; fill: var(--green); stroke: var(--green); }
</style>
</head>
<body>
  <section class="card card--front">
    <div class="brand">
      <span class="brand-square"></span>
      <span class="brand-name">Drainora</span>
    </div>
    <span class="divider"></span>
    <div class="details">
      <ul class="services">
        <li>Septic Pumping</li>
        <li>Installations/Repairs</li>
        <li>Restroom Rentals</li>
        <li>24/7 Emergency Service.</li>
      </ul>
    </div>
  </section>

  <section class="card card--back">
    <div class="brand">
      <span class="brand-square"></span>
      <span class="brand-name">Drainora</span>
    </div>
    <span class="divider"></span>
    <div class="details">
      <p class="person-name">DALE PRUITT</p>
      <p class="person-role">Owner &amp; Operator</p>
      <p class="address">812 Birchwell Lane<br>Fernwick PA 18999</p>
      <ul class="contact">
        <li>
          <svg viewBox="0 0 12 12" aria-hidden="true"><path stroke="none" d="M2.2 1 L4.2 1 L5 3.4 L3.8 4.4 C4.4 5.8 5.8 7.4 7.4 8 L8.4 6.9 L11 7.6 L11 9.8 C11 10.5 10.4 11 9.8 11 C5 10.6 1.2 6.8 1 2.2 C1 1.5 1.5 1 2.2 1 Z"/></svg>
          610-555-0187
        </li>
        <li>
          <svg viewBox="0 0 12 12" aria-hidden="true"><rect x="0.5" y="2.5" width="11" height="7" stroke="none"/><path d="M0.8 2.8 L6 6.6 L11.2 2.8" fill="none" stroke="#f7f7f7" stroke-width="1"/></svg>
          service@drainora.example
        </li>
        <li>
          <svg viewBox="0 0 12 12" aria-hidden="true"><circle cx="6" cy="6" r="5.2" fill="none" stroke-width="1.2"/><ellipse cx="6" cy="6" rx="2.2" ry="5.2" fill="none" stroke-width="1"/><path d="M0.8 6 H11.2" stroke-width="1" fill="none"/></svg>
          www.drainora.example
        </li>
      </ul>
    </div>
  </section>
</body>
</html>
```